Business Card design for Recruiter providing Recruitment Staff Augmentation services

I need a double sided business card. I have used Zek to print cards in the past and really like their quality. I have a logo but need to change the tagline that is part of the graphic.

The tagline currently reads and Connnecting people with careers - but it should be removed.

The back should look like a notecard for writing a to do list with the first to-do Augment Recruiting Staff

```html
<!DOCTYPE html>
<html lang="en">
<head>
<meta charset="utf-8">
<title>Talent Bay – Business Card</title>
<link rel="stylesheet" href="https://fonts.googleapis.com/css2?family=Source+Sans+3:wght@400;600&display=swap">
<style>
  :root {
    --stage: #4d3540;
    --paper: #ffffff;
    --navy: #123f5e;
    --rust: #c9522f;
    --line: #1f4e6e;
    --s-salmon: #f06a6a;
    --s-pink: #d66db1;
    --s-green: #5bbd58;
    --s-blue: #4a6fb5;
    --s-orange: #f6a030;
    --s-sky: #5aa5d8;
    --s-red: #e6363d;
  }
  * { box-sizing: border-box; margin: 0; padding: 0; }
  html, body { width: 1200px; height: 1200px; overflow: hidden; }
  body {
    background: var(--stage);
    font-family: "Source Sans 3", sans-serif;
    position: relative;
  }
  .card {
    position: absolute;
    left: 286px;
    width: 629px;
    height: 410px;
    background: var(--paper);
    overflow: hidden;
  }
  .card--front { top: 158px; }
  .card--back { top: 634px; }

  /* Front */
  .brand {
    position: absolute;
    left: 0;
    right: 0;
    top: 76px;
    text-align: center;
  }
  .brand__name {
    font-weight: 600;
    font-size: 54px;
    letter-spacing: 2px;
    color: var(--navy);
    line-height: 1;
  }
  .accent-bar {
    position: absolute;
    left: 0; top: 278px;
    width: 15px; height: 28px;
    background: var(--rust);
  }
  .person {
    position: absolute;
    left: 39px; top: 276px;
    font-size: 26px;
    color: var(--rust);
    font-weight: 400;
  }
  .contact {
    position: absolute;
    left: 39px; top: 328px;
    list-style: none;
    font-size: 18px;
    color: var(--navy);
    line-height: 22px;
  }
  .contact li { display: flex; align-items: center; gap: 6px; }
  .contact svg { width: 16px; height: 14px; fill: var(--rust); }
  .swoosh { position: absolute; left: 0; top: 0; }

  /* Back */
  .step {
    position: absolute;
    width: 162px;
    height: 37px;
  }
  .step__band {
    position: absolute;
    left: 18px; top: 3px;
    width: 144px; height: 31px;
    border-radius: 0 3px 3px 0;
    color: #fff;
    font-size: 8.5px;
    line-height: 10px;
    padding: 0 6px 0 26px;
    display: flex;
    align-items: center;
  }
  .step__icon {
    position: absolute;
    left: 0; top: 0;
    width: 37px; height: 37px;
    border-radius: 50%;
    border: 2px solid #fff;
    display: flex; align-items: center; justify-content: center;
  }
  .step__icon svg { width: 18px; height: 18px; fill: none; stroke: #fff; stroke-width: 1.6; }
  .step__num {
    position: absolute;
    right: -6px; top: -6px;
    width: 17px; height: 17px;
    border-radius: 50%;
    border: 1.5px solid #fff;
    color: #fff;
    font-size: 7.5px;
    display: flex; align-items: center; justify-content: center;
  }
  .step--salmon .step__band, .step--salmon .step__icon, .step--salmon .step__num { background: var(--s-salmon); }
  .step--pink .step__band, .step--pink .step__icon, .step--pink .step__num { background: var(--s-pink); }
  .step--green .step__band, .step--green .step__icon, .step--green .step__num { background: var(--s-green); }
  .step--blue .step__band, .step--blue .step__icon, .step--blue .step__num { background: var(--s-blue); }
  .step--orange .step__band, .step--orange .step__icon, .step--orange .step__num { background: var(--s-orange); }
  .step--sky .step__band, .step--sky .step__icon, .step--sky .step__num { background: var(--s-sky); }
  .step--red .step__band, .step--red .step__icon, .step--red .step__num { background: var(--s-red); }

  .note-line {
    position: absolute;
    left: 45px;
    width: 535px;
    height: 1.5px;
    background: var(--line);
  }
</style>
</head>
<body>

<section class="card card--front">
  <div class="brand">
    <div class="brand__name">TALENT BAY</div>
  </div>

  <div class="accent-bar"></div>
  <div class="person">Dana Whitfield, SPHR</div>
  <ul class="contact">
    <li><svg viewBox="0 0 16 12"><path d="M0 0h16v12H0z M1 1.5l7 5 7-5" stroke="#fff" stroke-width="1.2"/></svg>dana@talentbay.com</li>
    <li><svg viewBox="0 0 16 14"><path d="M1 5c0-3 14-3 14 0v1h-4V4H5v2H1z M3 7h10l1 6H2z"/><circle cx="8" cy="10" r="1.6" fill="#fff"/></svg>555-014-2298</li>
  </ul>

  <svg class="swoosh" width="629" height="410" viewBox="0 0 629 410">
    <path d="M162 410 C 270 330 480 300 629 398 L629 406 C 480 320 300 350 221 410 Z" fill="var(--rust)"/>
  </svg>
</section>

<section class="card card--back">
  <div class="step step--salmon" style="left:36px; top:66px;">
    <div class="step__band">Employees' Requirements<br>Analysis.</div>
    <div class="step__icon"><svg viewBox="0 0 18 18"><path d="M4 3h7l3 3v9H4z"/></svg></div>
    <div class="step__num">01</div>
  </div>
  <div class="step step--green" style="left:227px; top:66px;">
    <div class="step__band">Publishing Job Vacancy<br>Ads by Crestline.</div>
    <div class="step__icon"><svg viewBox="0 0 18 18"><circle cx="9" cy="5" r="2.5"/><path d="M4 15v-4h10v4z"/></svg></div>
    <div class="step__num">02</div>
  </div>
  <div class="step step--sky" style="left:413px; top:66px;">
    <div class="step__band">CV Review and Selection.</div>
    <div class="step__icon"><svg viewBox="0 0 18 18"><path d="M4 2h10v14H4z M6 6h6 M6 9h6 M6 12h4"/></svg></div>
    <div class="step__num">03</div>
  </div>

  <div class="step step--pink" style="left:36px; top:115px;">
    <div class="step__band">Conducting Test and In-Depth<br>Interviews.</div>
    <div class="step__icon"><svg viewBox="0 0 18 18"><circle cx="5" cy="5" r="2"/><circle cx="13" cy="5" r="2"/><path d="M2 15v-5h6v5 M10 15v-5h6v5"/></svg></div>
    <div class="step__num">04</div>
  </div>
  <div class="step step--blue" style="left:227px; top:115px;">
    <div class="step__band">Selection of the Employee<br>and Agreement.</div>
    <div class="step__icon"><svg viewBox="0 0 18 18"><circle cx="9" cy="6" r="3.5"/><path d="M2 14c3-2 5 0 7 0s5-2 7 0"/></svg></div>
    <div class="step__num">05</div>
  </div>
  <div class="step step--red" style="left:413px; top:115px;">
    <div class="step__band">Matching Candidates with<br>Company for Final Selection.</div>
    <div class="step__icon"><svg viewBox="0 0 18 18"><circle cx="9" cy="9" r="7"/><path d="M5.5 9l2.5 2.5 4.5-5"/></svg></div>
    <div class="step__num">06</div>
  </div>

  <div class="step step--orange" style="left:227px; top:165px;">
    <div class="step__band">Selecting the Best<br>Candidates for the Job.</div>
    <div class="step__icon"><svg viewBox="0 0 18 18"><path d="M3 8h3v7H3z M6 8l3-5c1.5 0 2 1 1.5 2.5L10 8h4.5l-1.5 7H6"/></svg></div>
    <div class="step__num">07</div>
  </div>

  <div class="note-line" style="top:251px;"></div>
  <div class="note-line" style="top:284px;"></div>
  <div class="note-line" style="top:318px;"></div>
  <div class="note-line" style="top:351px;"></div>
</section>

</body>
</html>
```